Country House in Italy Needs a Business Card Design

We need a business card design for “Casale del Ginepro”, a modern concept of a Farm Holidays/Country House to be opened in central Italy.
Attached is the company logo you did for us in the past.
Please
- create a double-sided business card design
- on the back I would like to have the logo
- on the front the copy
Copy on card:
o Casale del Ginepro
o Address: Via Pontemurra, 14
Cingoli (MC), Italy
o Website: www.casaledelginepro.it
o Email: info@casaledelginepro.it
o my name : Marisa
o my mobile phone number: +39 347 8123905
In the distribution of information keep in mind the possible inclusion also of a landline telephone number (currently not available / existing).
WE WOULD LIKE TO HAVE A MODERN, PROFFESIONAL, OUT OF THE BOX BUSINESS CARD. BE AS CREATIVE AS YOU WOULD LIKE.

```html
<!DOCTYPE html>
<html lang="it">
<head>
<meta charset="utf-8">
<title>Casale del Ginepro – Business Card</title>
<link rel="stylesheet" href="https://fonts.googleapis.com/css2?family=Lato:wght@400;700;900&family=Lustria&display=swap">
<style>
  :root {
    --stage: #2e2e2e;
    --card: #fbfbfa;
    --orange: #e0793a;
    --gold: #8c7546;
    --brand-brown: #5b4631;
    --ink: #262626;
    --pattern: #f1ddd0;
  }
  * { box-sizing: border-box; margin: 0; padding: 0; }
  html, body { width: 1200px; height: 900px; overflow: hidden; }
  body { background: var(--stage); font-family: "Lato", Arial, sans-serif; position: relative; }

  .card {
    position: absolute; width: 620px; height: 354px;
    background: var(--card); border-radius: 3px; overflow: hidden;
    box-shadow: 0 14px 30px rgba(0,0,0,.45);
  }
  .card--back { left: 60px; top: 64px; }
  .card--front { left: 520px; top: 478px; }

  .pattern-area {
    position: absolute; border-radius: 50%;
    background: radial-gradient(circle, var(--pattern) 0%, rgba(241,221,208,.55) 45%, rgba(241,221,208,0) 70%);
  }
  .card--back .pattern-area--top { width: 260px; height: 260px; right: -70px; top: -90px; }
  .card--back .pattern-area--bottom { width: 260px; height: 260px; left: -90px; bottom: -80px; }
  .card--front .pattern-area--side { width: 300px; height: 300px; right: -110px; top: -10px; }

  .brand { display: flex; flex-direction: column; align-items: center; gap: 14px; }
  .brand-mark { width: 70px; height: 70px; border-radius: 50%; background: var(--orange); }
  .brand-name { font-family: "Lustria", Georgia, serif; color: var(--brand-brown); font-size: 38px; font-weight: 400; white-space: nowrap; }

  .card--back .brand { position: absolute; left: 0; right: 0; top: 96px; }

  .card--front .brand { position: absolute; left: 50px; top: 28px; }
  .card--front .brand-mark { width: 58px; height: 58px; }
  .card--front .brand-name { font-size: 30px; }

  .holder { position: absolute; right: 36px; top: 30px; text-align: right; }
  .holder-name { color: var(--gold); font-weight: 900; font-size: 20px; letter-spacing: .5px; text-transform: uppercase; }
  .holder-role { color: var(--ink); font-weight: 700; font-size: 14px; }

  .address { position: absolute; left: 50px; top: 178px; color: var(--gold); font-weight: 900; font-size: 14.5px; text-transform: uppercase; letter-spacing: .2px; white-space: nowrap; }

  .contacts {
    position: absolute; left: 50px; top: 222px; list-style: none;
    display: grid; grid-template-columns: 230px 260px; row-gap: 18px;
    font-weight: 700; color: var(--ink); font-size: 16px;
  }
  .contacts li { display: flex; align-items: center; gap: 10px; white-space: nowrap; }
  .contacts svg { width: 18px; height: 18px; flex: none; }
  .contacts .icon { fill: none; stroke: var(--gold); stroke-width: 2; stroke-linecap: round; stroke-linejoin: round; }
  .contacts .icon-solid { fill: var(--gold); }
</style>
</head>
<body>

  <section class="card card--back" aria-label="Card back with brand name">
    <div class="pattern-area pattern-area--top" role="img" aria-label="Faint decorative mosaic pattern"></div>
    <div class="pattern-area pattern-area--bottom" role="img" aria-label="Faint decorative mosaic pattern"></div>
    <div class="brand">
      <span class="brand-mark"></span>
      <span class="brand-name">Casale del Ginepro</span>
    </div>
  </section>

  <section class="card card--front" aria-label="Card front with contact details">
    <div class="pattern-area pattern-area--side" role="img" aria-label="Faint decorative mosaic pattern"></div>

    <div class="brand">
      <span class="brand-mark"></span>
      <span class="brand-name">Casale del Ginepro</span>
    </div>

    <div class="holder">
      <p class="holder-name">Marisa</p>
      <p class="holder-role">Designation</p>
    </div>

    <p class="address">Via/Località Pontemurra, 14 62099 Valdorano (VD), Italy</p>

    <ul class="contacts">
      <li>
        <svg viewBox="0 0 18 18" aria-hidden="true"><rect class="icon" x="5" y="1.5" width="8" height="15" rx="1.5"/><line class="icon" x1="8" y1="14" x2="10" y2="14"/></svg>
        +39 347 8123905
      </li>
      <li>
        <svg viewBox="0 0 18 18" aria-hidden="true"><path class="icon-solid" d="M4 1.5l3 3.2-1.6 2.2c.9 2 2.4 3.6 4.6 4.7l2.1-1.6 3.4 3-1.7 2.9C8.3 15.6 2.3 9.7 1.3 3.6z"/></svg>
        0733 604 218
      </li>
      <li>
        <svg viewBox="0 0 18 18" aria-hidden="true"><rect class="icon-solid" x="1" y="3.5" width="16" height="11" rx="1"/><path d="M1.5 4.2L9 10l7.5-5.8" fill="none" stroke="#fbfbfa" stroke-width="1.4"/></svg>
        info@casaledelginepro.it
      </li>
      <li>
        <svg viewBox="0 0 18 18" aria-hidden="true"><path class="icon" d="M7.5 10.5a3 3 0 0 0 4.2 0l3-3a3 3 0 0 0-4.2-4.2l-1 1"/><path class="icon" d="M10.5 7.5a3 3 0 0 0-4.2 0l-3 3a3 3 0 0 0 4.2 4.2l1-1"/></svg>
        www.casaledelginepro.it
      </li>
    </ul>
  </section>

</body>
</html>
```